Creative Fitness Studio Feature Wall

Two feature walls within functional fitness studio, they need to be on brand and have a WOW factor.
Designed to inspire and motivate people to live a fit and healthy lifestyle whilst working out and bringing life to the studio, as an uplifting and inviting environment.

Please see current walls and also visit website www.velta4.com.au for inspiration.
Updates

Target Market(s)

health and fitness, healthy lifestyle

Industry/Entity Type

Fitness

Font styles to use
Other font styles liked:
• gothic

Colors

Designer to choose colors to be used in the design.

Requirements
Must have
• inspiration from website www.velta4.com.au ........... brand consistency
Nice to have
• WOW factor......... walk into the gym and it draws your attention.
Should not have
• Overly muscly people (bodybuilders)

```html
<!DOCTYPE html>
<html lang="en">
<head>
<meta charset="utf-8">
<title>Velta4 Fitness – Feature Wall</title>
<link rel="stylesheet" href="https://fonts.googleapis.com/css2?family=Open+Sans:wdth,wght@75..100,300..800&display=swap">
<style>
  :root {
    --brand-green: #8cc63f;
    --brand-charcoal: #4a4a4a;
    --brand-slate: #5c5c5c;
    --ink: #111111;
    --paper: #ffffff;
    --backdrop: #ececec;
  }
  html, body {
    margin: 0;
    width: 1200px;
    height: 800px;
    overflow: hidden;
    background: var(--backdrop);
  }
  .feature-wall {
    position: absolute;
    left: 215px;
    top: 15px;
    width: 770px;
    height: 770px;
    display: block;
    font-family: "Open Sans", Arial, sans-serif;
    font-stretch: 75%;
  }
  .wall-base { fill: var(--paper); }
  .fill-green { fill: var(--brand-green); }
  .fill-charcoal { fill: var(--brand-charcoal); }
  .fill-slate { fill: var(--brand-slate); }
  .quote-strong { font-weight: 700; }
  .quote-light { font-weight: 300; }
  .text-green { fill: var(--brand-green); }
  .text-white { fill: var(--paper); }
  .text-charcoal { fill: var(--brand-charcoal); }
  .brand-name { font-weight: 800; fill: var(--ink); font-stretch: 100%; letter-spacing: -1px; }
  .brand-tag { font-weight: 400; fill: var(--ink); font-stretch: 100%; letter-spacing: 4px; }
  .gap { stroke: var(--paper); stroke-width: 5; }
</style>
</head>
<body>
<svg class="feature-wall" viewBox="0 0 885 885" xmlns="http://www.w3.org/2000/svg">
  <defs>
    <linearGradient id="tone-boxing" x1="0" y1="0" x2="1" y2="1">
      <stop offset="0" stop-color="#6a1414"/><stop offset="0.5" stop-color="#1d2a30"/><stop offset="1" stop-color="#0f3a3a"/>
    </linearGradient>
    <linearGradient id="tone-sunset" x1="0" y1="0" x2="0" y2="1">
      <stop offset="0" stop-color="#7a5a2a"/><stop offset="0.6" stop-color="#e7a53a"/><stop offset="1" stop-color="#2a1c10"/>
    </linearGradient>
    <linearGradient id="tone-studio" x1="0" y1="0" x2="1" y2="1">
      <stop offset="0" stop-color="#3a3a3a"/><stop offset="1" stop-color="#b8b4b0"/>
    </linearGradient>
    <linearGradient id="tone-mono" x1="0" y1="0" x2="1" y2="1">
      <stop offset="0" stop-color="#1c1c1c"/><stop offset="1" stop-color="#6a6a6a"/>
    </linearGradient>
    <linearGradient id="tone-gym" x1="0" y1="0" x2="0" y2="1">
      <stop offset="0" stop-color="#e6e2e4"/><stop offset="0.7" stop-color="#8a4a48"/><stop offset="1" stop-color="#3a2a2a"/>
    </linearGradient>
    <linearGradient id="tone-road" x1="0" y1="0" x2="0" y2="1">
      <stop offset="0" stop-color="#5a78a8"/><stop offset="0.55" stop-color="#5f8a3e"/><stop offset="1" stop-color="#a8a8a8"/>
    </linearGradient>
    <linearGradient id="tone-class" x1="0" y1="0" x2="1" y2="1">
      <stop offset="0" stop-color="#cfd3d8"/><stop offset="1" stop-color="#3c4a66"/>
    </linearGradient>
    <linearGradient id="tone-meadow" x1="0" y1="0" x2="1" y2="1">
      <stop offset="0" stop-color="#8cc63f"/><stop offset="1" stop-color="#4e8a2a"/>
    </linearGradient>
    <linearGradient id="tone-bright" x1="0" y1="0" x2="0" y2="1">
      <stop offset="0" stop-color="#f2ede8"/><stop offset="1" stop-color="#c9a898"/>
    </linearGradient>
    <linearGradient id="tone-brick" x1="0" y1="0" x2="1" y2="0">
      <stop offset="0" stop-color="#2a2626"/><stop offset="1" stop-color="#5a4a44"/>
    </linearGradient>
  </defs>

  <rect class="wall-base" x="0" y="0" width="885" height="885"/>

  <!-- Panel: one life one chance -->
  <g class="panel panel-one-chance">
    <rect class="fill-charcoal" x="15" y="12" width="492" height="296"/>
    <polygon role="img" aria-label="Boxer in gloves ready to train" fill="url(#tone-boxing)" points="15,12 150,12 340,212 262,308 15,308"/>
    <polygon role="img" aria-label="Yoga pose silhouetted against a sunset" fill="url(#tone-sunset)" points="165,12 500,12 344,205"/>
    <polygon role="img" aria-label="Smiling athlete in training wear" fill="url(#tone-studio)" points="507,22 507,308 430,308 356,220"/>
    <polygon class="fill-green" points="344,228 266,308 422,308"/>
    <text x="198" y="223" font-size="38"><tspan class="quote-strong text-green">ONE</tspan><tspan class="quote-light text-white" font-size="28" dx="8">life</tspan></text>
    <text class="quote-light text-white" x="182" y="248" font-size="28">one</text>
    <text class="quote-strong text-green" x="156" y="283" font-size="38">CHANCE</text>
  </g>

  <rect class="fill-green" x="520" y="12" width="18" height="296"/>

  <!-- Panel: challenge -->
  <g class="panel panel-challenge">
    <rect role="img" aria-label="Athlete sprinting, black and white" fill="url(#tone-mono)" x="552" y="12" width="318" height="296"/>
    <polygon class="fill-green" points="565,308 870,28 870,308"/>
    <g text-anchor="end">
      <text class="quote-light text-charcoal" x="862" y="180" font-size="26">if it doesn’t</text>
      <text class="quote-strong text-charcoal" x="862" y="210" font-size="36">CHALLENGE</text>
      <text class="quote-light text-charcoal" x="862" y="247" font-size="38">you, it doesnt</text>
      <text x="862" y="296" font-size="46"><tspan class="quote-strong text-charcoal">CHANGE</tspan><tspan class="quote-light text-charcoal" dx="8">YOU</tspan></text>
    </g>
  </g>

  <!-- Panel: attitude -->
  <g class="panel panel-attitude">
    <rect role="img" aria-label="Suspension strap training in the gym" fill="url(#tone-gym)" x="15" y="322" width="492" height="256"/>
    <polygon class="fill-slate" points="15,322 245,322 40,578 15,578"/>
    <text class="quote-strong text-green" x="25" y="374" font-size="38">ATTITUDE</text>
    <text class="quote-light text-white" x="25" y="400" font-size="21">determins how well</text>
    <text class="quote-light text-white" x="25" y="424" font-size="21">you do it</text>
  </g>

  <!-- Brand block -->
  <g class="brand-block" text-anchor="middle">
    <text class="brand-name" x="696" y="368" font-size="52">VELTA4</text>
    <text class="brand-tag" x="696" y="391" font-size="15">FITNESS</text>
  </g>

  <!-- Panel: getting ahead -->
  <g class="panel panel-ahead">
    <rect role="img" aria-label="Cyclist riding on an open road" fill="url(#tone-road)" x="524" y="405" width="344" height="172"/>
    <polygon class="fill-slate" points="524,405 702,405 657,577 524,577"/>
    <text x="537" y="455" font-size="22"><tspan class="quote-light text-white">The secret</tspan><tspan class="quote-light text-white" font-size="18"> of getting</tspan></text>
    <text class="quote-strong text-green" x="537" y="490" font-size="36">AHEAD</text>
    <text class="quote-light text-white" x="537" y="513" font-size="21">is getting</text>
    <text class="quote-strong text-green" x="537" y="545" font-size="29">STARTED</text>
  </g>

  <!-- Panel: motivation and habit -->
  <g class="panel panel-habit">
    <rect role="img" aria-label="Meditation outdoors on the grass" fill="url(#tone-meadow)" x="15" y="590" width="492" height="255"/>
    <polygon role="img" aria-label="Group class doing sit-ups on mats" fill="url(#tone-class)" points="15,590 125,590 325,845 15,845"/>
    <line class="gap" x1="125" y1="590" x2="325" y2="845"/>
    <text class="quote-strong text-white" x="185" y="628" font-size="32">MOTIVATION</text>
    <text class="quote-light text-white" x="196" y="648" font-size="19">is what gets you started.</text>
    <text class="quote-strong text-white" x="217" y="678" font-size="32">HABIT</text>
    <text class="quote-light text-white" x="236" y="698" font-size="19">is what keeps you</text>
    <text class="quote-strong text-white" x="249" y="729" font-size="32">GOING</text>
  </g>

  <!-- Panel: ability -->
  <g class="panel panel-ability">
    <rect role="img" aria-label="Athlete measuring her waist" fill="url(#tone-bright)" x="524" y="590" width="121" height="248"/>
    <rect class="fill-charcoal" x="655" y="590" width="211" height="136"/>
    <rect class="fill-green" x="655" y="694" width="42" height="33"/>
    <rect role="img" aria-label="Two people doing pull-ups against a brick wall" fill="url(#tone-brick)" x="655" y="734" width="211" height="104"/>
    <text class="quote-strong text-green" x="667" y="628" font-size="27">ABILITY</text>
    <text class="quote-light text-white" x="667" y="648" font-size="17">is what you’re capable of doing.</text>
    <text class="quote-strong text-green" x="667" y="681" font-size="27">MOTIVATION</text>
    <text class="quote-light text-white" x="708" y="702" font-size="17">determines what you do.</text>
  </g>

  <!-- Base band -->
  <rect class="fill-charcoal" x="0" y="855" width="885" height="27"/>
  <polygon class="fill-green" points="732,855 885,855 885,882 760,882"/>
</svg>
</body>
</html>
```